BrovaLT BIZ Card, email signature & Stationary

Professional business cards, email signatures and ms word letterhead

Target Market(s)

business owners

Industry/Entity Type

cloud hosting

Contact Information for Business Card

name title office phone number , direct line, fax email address web site

Font styles to use
Other font styles liked:
• something that compliments font in logo

```html
<!DOCTYPE html>
<html lang="en">
<head>
<meta charset="utf-8">
<title>BrovaLT Business Card</title>
<link href="https://fonts.googleapis.com/css2?family=Roboto:wght@300;400;700&display=swap" rel="stylesheet">
<style>
  :root {
    --brand-red: #ff0a00;
    --ink: #222222;
    --rule: #444444;
    --paper: #ffffff;
    --backdrop: #1c1c1c;
    --band-black: #050505;
  }
  * { margin: 0; padding: 0; box-sizing: border-box; }
  html, body { width: 900px; height: 1200px; overflow: hidden; }
  body {
    background: var(--backdrop);
    font-family: "Roboto", Arial, sans-serif;
    position: relative;
  }
  .card { position: absolute; left: 135px; width: 645px; }
  .card-front {
    top: 218px; height: 364px;
    background: var(--brand-red);
    display: flex; align-items: center; justify-content: center;
  }
  .wordmark {
    font-family: "Roboto", Arial, sans-serif;
    font-weight: 300;
    letter-spacing: -2px;
    line-height: 1;
  }
  .card-front .wordmark { color: var(--paper); font-size: 112px; }
  .card-back {
    top: 628px; height: 372px;
    background: var(--paper);
    overflow: hidden;
  }
  .card-back .wordmark {
    position: absolute; right: 40px; top: 34px;
    color: var(--brand-red); font-size: 96px;
  }
  .person { position: absolute; left: 35px; top: 180px; }
  .person-name { color: var(--brand-red); font-weight: 700; font-size: 25px; }
  .person-title { color: var(--ink); font-size: 17px; margin-top: 6px; }
  .divider {
    position: absolute; left: 35px; width: 572px; top: 262px;
    border-top: 1.5px solid var(--rule);
  }
  .contacts { position: absolute; top: 276px; list-style: none; }
  .contacts-left { left: 35px; }
  .contacts-right { left: 418px; top: 272px; }
  .contacts li {
    display: flex; align-items: center; gap: 14px;
    font-size: 18px; color: var(--ink); height: 24px;
  }
  .contacts svg { width: 17px; height: 17px; fill: var(--brand-red); flex: none; }
  .footer-band { position: absolute; left: 0; bottom: 0; width: 645px; height: 34px; }
  .web {
    position: absolute; right: 56px; bottom: 10px;
    color: var(--paper); font-size: 17px;
  }
</style>
</head>
<body>
  <section class="card card-front">
    <div class="wordmark">BrovaLT</div>
  </section>

  <section class="card card-back">
    <div class="wordmark">BrovaLT</div>

    <div class="person">
      <div class="person-name">Daniel Marsh</div>
      <div class="person-title">Owner</div>
    </div>

    <div class="divider"></div>

    <ul class="contacts contacts-left">
      <li>
        <svg viewBox="0 0 24 24" aria-hidden="true"><path d="M2 9c0-3 5-5 10-5s10 2 10 5v2h-5V8.5c-1.5-.6-3.3-.9-5-.9s-3.5.3-5 .9V11H2zM6 12l2-3h8l2 3v8H6zm4 2v1.5h1.5V14zm2.5 0v1.5H14V14zm-2.5 3v1.5h1.5V17zm2.5 0v1.5H14V17z"/></svg>
        555.014.2290
      </li>
      <li>
        <svg viewBox="0 0 24 24" aria-hidden="true"><path d="M6.6 10.8a15 15 0 0 0 6.6 6.6l2.2-2.2c.3-.3.7-.4 1-.2 1.1.4 2.3.6 3.6.6.6 0 1 .4 1 1V20c0 .6-.4 1-1 1A17 17 0 0 1 3 4c0-.6.4-1 1-1h3.5c.6 0 1 .4 1 1 0 1.3.2 2.5.6 3.6.1.3 0 .7-.2 1z"/></svg>
        555.014.2291
      </li>
    </ul>

    <ul class="contacts contacts-right">
      <li>
        <svg viewBox="0 0 24 24" aria-hidden="true"><path d="M3 8h3v13H3zm5-5h9v5h3v13H8zm2 2v3h5V5zm1 6v2h2v-2zm4 0v2h2v-2zm-4 4v2h2v-2zm4 0v2h2v-2z"/></svg>
        555.014.2292
      </li>
      <li>
        <svg viewBox="0 0 24 24" aria-hidden="true"><path d="M2 5h20v14H2zm2 2v.5l8 5.5 8-5.5V7l-8 5.2z"/></svg>
        info@brovaltcloud.com
      </li>
    </ul>

    <svg class="footer-band" viewBox="0 0 645 34" preserveAspectRatio="none" aria-hidden="true">
      <path d="M0 6 H375 Q366 14 356 20 H0 Z" fill="var(--band-black)"/>
      <path d="M0 23 H370 Q388 6 405 0 H645 V34 H0 Z" fill="var(--brand-red)"/>
    </svg>
    <div class="web">www.brovaltcloud.com</div>
  </section>
</body>
</html>
```